RivoCounsel Compensation Lawyers

We need a modern, sleek letterhead that is professional.

In relation to the footer, we would like to have firm contact details there ideally, however you must also insert at the bottom of each page the following....

Liability limited by a scheme approved under the Professional Standards Legislation.

From the attachment you can extract the firm logo. Also, I would like the Accredited specialist circle on the letterhead also.

Also, I would like you to create a document that can easily be edited for change of contact details, as these are likely to change.

Industry/Entity Type

It Professional

Font styles to use
Sans Serif

Colors
0655a3
3276b5
85abd2
0492cd
33a6d7
85cae6
cee9f5
eaf1f7
cbcbcb

Requirements
Must have
• Ph: 8371-5264
• F: 8815-3927
• M 0468-253-914
• mk@rivocounsel.example.au
• www.rivocounsel.example.au
Nice to have
• the word document gives you an idea of what I like. I am happy for your to amaze me with your creativity.

```html
<!DOCTYPE html>
<html lang="en">
<head>
<meta charset="utf-8">
<title>RivoCounsel Compensation Lawyers – Letterhead</title>
<link href="https://fonts.googleapis.com/css2?family=Roboto:wght@400;700&display=swap" rel="stylesheet">
<style>
  :root {
    --brand-blue: #0655a3;
    --brand-mid: #3276b5;
    --brand-light: #85abd2;
    --brand-cyan: #0492cd;
    --rule-blue: #3276b5;
    --ink: #1d1f22;
    --ink-soft: #3a3d42;
    --paper: #ffffff;
    --backdrop: #e9eaec;
    --badge-ring: #4a4d52;
  }
  * { margin: 0; padding: 0; box-sizing: border-box; }
  html, body {
    width: 1200px;
    height: 936px;
    overflow: hidden;
    background: var(--backdrop);
    font-family: "Roboto", Arial, sans-serif;
  }
  .canvas {
    position: relative;
    width: 1200px;
    height: 936px;
  }
  .letterhead {
    position: absolute;
    left: 289px;
    top: 28px;
    width: 622px;
    height: 880px;
    background: var(--paper);
    box-shadow: 0 2px 10px rgba(0,0,0,0.10);
  }
  .brand {
    position: absolute;
    left: 56px;
    top: 58px;
    display: flex;
    align-items: center;
    gap: 10px;
  }
  .brand-dot {
    width: 26px;
    height: 26px;
    border-radius: 50%;
    background: var(--brand-cyan);
  }
  .brand-name {
    font-size: 17px;
    font-weight: 400;
    color: var(--brand-blue);
    letter-spacing: 0.1px;
  }
  .accreditation-badge {
    position: absolute;
    right: 46px;
    bottom: 150px;
    width: 42px;
    height: 42px;
    border-radius: 50%;
    border: 2px solid var(--badge-ring);
    background: radial-gradient(circle, var(--brand-mid) 0 38%, var(--paper) 40%);
  }
  .footer {
    position: absolute;
    left: 56px;
    right: 46px;
    bottom: 40px;
    display: flex;
    justify-content: space-between;
    align-items: flex-end;
  }
  .footer-block {
    border-left: 2px solid var(--rule-blue);
    padding-left: 8px;
    font-size: 8.5px;
    font-weight: 700;
    line-height: 1.4;
    color: var(--ink);
  }
  .address-group + .address-group { margin-top: 6px; }
  .contact-list { list-style: none; }
  .contact-list li {
    display: flex;
    align-items: center;
    gap: 5px;
  }
  .contact-list svg {
    width: 9px;
    height: 9px;
    flex: none;
  }
  .liability {
    width: 118px;
    color: var(--ink-soft);
  }
</style>
</head>
<body>
<div class="canvas">
  <main class="letterhead">
    <header class="brand">
      <span class="brand-dot"></span>
      <span class="brand-name">RivoCounsel Compensation Lawyers</span>
    </header>

    <div class="accreditation-badge" role="img" aria-label="Accredited specialist seal"></div>

    <footer class="footer">
      <address class="footer-block address" style="font-style:normal">
        <div class="address-group">14/82 Harbourline Road<br>Westmere NSW 2291</div>
        <div class="address-group">P.O. Box K418<br>Northvale NSW 2187</div>
      </address>

      <ul class="footer-block contact-list">
        <li>
          <svg viewBox="0 0 10 10" aria-hidden="true"><path d="M2 1h2l1 2-1.2 1a5 5 0 0 0 2.2 2.2L7 5l2 1v2c0 .6-.4 1-1 1A8 8 0 0 1 1 2c0-.6.4-1 1-1z" fill="var(--ink)"/></svg>
          (02) 8371 5264
        </li>
        <li>
          <svg viewBox="0 0 10 10" aria-hidden="true"><rect x="1" y="4" width="8" height="5" fill="var(--ink)"/><rect x="3" y="1" width="4" height="3" fill="none" stroke="var(--ink)"/></svg>
          (02) 8815 3927
        </li>
        <li>
          <svg viewBox="0 0 10 10" aria-hidden="true"><rect x="1" y="2.5" width="8" height="5.5" fill="none" stroke="var(--ink)"/><path d="M1 2.5l4 3 4-3" fill="none" stroke="var(--ink)"/></svg>
          mk@rivocounsel.example.au
        </li>
        <li>
          <svg viewBox="0 0 10 10" aria-hidden="true"><rect x="3" y="1" width="4" height="8" rx="0.8" fill="none" stroke="var(--ink)"/><circle cx="5" cy="7.5" r="0.5" fill="var(--ink)"/></svg>
          0468 253 914
        </li>
        <li>
          <svg viewBox="0 0 10 10" aria-hidden="true"><circle cx="5" cy="5" r="4" fill="none" stroke="var(--ink)"/><path d="M1 5h8M5 1c-2 2.5-2 5.5 0 8M5 1c2 2.5 2 5.5 0 8" fill="none" stroke="var(--ink)" stroke-width="0.7"/></svg>
          www.rivocounsel.example.au
        </li>
      </ul>

      <p class="footer-block liability">Liability limited by a scheme approved under the Professional Standards Legislation.</p>
    </footer>
  </main>
</div>
</body>
</html>
```